Flyer/Poster design required for volunteer activities

We need a STRIKING A4 Poster/Flyer advertising our conservation volunteer program activities which are currently happening in the area. This poster is to advertise the program once people have arrived on the island or to locals. The program covers 5 months, May-September 2019 and is focused on conservation. I have attached the following:
- a flyer which was previously created (QMR Habitat Helpers 2019 sm)to advertise the program - would prefer it has a similar striking resemblance, but not essential
- A mock up document 'HHQMR On Island Poster_2019_v2' with text -Logos-Images

Target Market(s)

Everyone interested in Environmental Adventure/Hiking/Citizen Science

Industry/Entity Type

Tourism

Font styles to use
Sans Serif

Requirements
Must have
• -A travel conservation focus
• -Must use 'QMR-Background Image' as the background to the design
• -The info of where to get more information and the social media details must be prominent

```html
<!DOCTYPE html>
<html lang="en">
<head>
<meta charset="utf-8">
<title>QMR Habitat Helpers – May to September 2019</title>
<link href="https://fonts.googleapis.com/css2?family=Comfortaa:wght@700&family=Fira+Sans+Extra+Condensed:wght@400;500;600&family=Oswald:wght@300&family=Montserrat:wght@500&display=swap" rel="stylesheet">
<style>
  :root{
    --navy:#1d2b5a;
    --navy-deep:#121c3a;
    --orange:#f04e23;
    --orange-light:#f7a21b;
    --yellow:#fff04a;
    --cream:#fff5c2;
    --white:#ffffff;
  }
  *{margin:0;padding:0;box-sizing:border-box}
  html,body{width:848px;height:1200px;overflow:hidden;background:var(--white)}
  .poster{position:relative;width:848px;height:1200px;overflow:hidden;font-family:"Fira Sans Extra Condensed",sans-serif}
  .backdrop{position:absolute;left:22px;top:16px;width:804px;height:1176px;
    background:
      radial-gradient(ellipse 260px 520px at 60px 820px, rgba(74,98,48,.9), rgba(74,98,48,0) 70%),
      radial-gradient(ellipse 360px 260px at 160px 1120px, rgba(62,84,40,.95), rgba(62,84,40,0) 75%),
      radial-gradient(ellipse 260px 160px at 640px 170px, rgba(70,84,70,.75), rgba(70,84,70,0) 75%),
      radial-gradient(ellipse 320px 220px at 450px 780px, rgba(70,170,190,.55), rgba(70,170,190,0) 75%),
      linear-gradient(180deg,#c9dcec 0%,#a9c6de 12%,#3d7fb8 26%,#2f6fae 45%,#3f87a6 62%,#2b5170 80%,#1a2b3a 100%);}
  .frame{position:absolute;left:13px;top:10px;width:822px;height:1178px;border:4px solid var(--orange)}
  .badge{position:absolute;left:54px;top:26px;width:108px;height:108px;border-radius:50%;
    background:var(--white);border:4px solid var(--navy);display:flex;align-items:center;justify-content:center;text-align:center;
    font-family:"Comfortaa",sans-serif;font-weight:700;font-size:14px;line-height:1.2;color:var(--navy)}
  .title{position:absolute;right:40px;font-family:"Comfortaa",sans-serif;font-weight:700;letter-spacing:-1px;text-align:right;white-space:nowrap}
  .title-place{top:56px;font-size:78px;color:var(--navy)}
  .title-program{top:136px;font-size:64px;background:linear-gradient(180deg,var(--orange-light),var(--orange));-webkit-background-clip:text;background-clip:text;color:transparent}
  .dates{position:absolute;right:48px;top:192px;font-family:"Oswald",sans-serif;font-weight:300;font-size:38px;color:var(--white)}
  .call{position:absolute;left:104px;top:246px;width:654px;height:82px;border-radius:41px;background:var(--navy);border:3px solid var(--white);
    display:flex;flex-direction:column;justify-content:center;align-items:center;color:var(--yellow);font-weight:600;font-size:24px;line-height:1.25}
  .month{position:absolute;height:38px;border-radius:19px;background:var(--orange);color:var(--cream);font-weight:600;font-size:16px;
    display:flex;align-items:center;justify-content:center;white-space:nowrap}
  .photo{position:absolute;border-radius:50%;border:3px solid var(--white)}
  .feature{position:absolute;color:var(--white);font-size:10px;line-height:15.8px}
  .feature h2{font-weight:600;font-size:12px;line-height:18px;margin-bottom:2px}
  .feature p{font-weight:400}
  .feature.right{text-align:right}
  .info{position:absolute;left:130px;top:1090px;width:586px;height:90px;border-radius:45px;background:var(--navy-deep);border:3px solid var(--white);
    font-family:"Montserrat",sans-serif;font-weight:500;font-size:14px;line-height:19px;color:var(--white);text-align:center;padding-top:13px}
  .info .follow{display:flex;justify-content:flex-start;gap:20px;padding-left:44px}
  .info .links{color:#6fb3e6}
</style>
</head>
<body>
<main class="poster">
  <div class="backdrop" role="img" aria-label="Aerial photograph of the island lagoon, coral reef and mountains"></div>
  <div class="frame"></div>

  <div class="badge">QMR<br>Habitat<br>Helpers</div>

  <h1 class="title title-place">queen mary reef</h1>
  <div class="title title-program">habitat helpers</div>
  <div class="dates">May – September 2019</div>

  <div class="call"><span>BE INVOLVED IN PROTECTING PARADISE</span><span>JOIN THE QMR HABITAT HELPERS PROGRAM 2019</span></div>

  <!-- May -->
  <div class="month" style="left:72px;top:352px;width:270px">MAY 2019&nbsp; Feature Week: 19th – 26th May</div>
  <div class="photo" role="img" aria-label="Photo of a seabird chick on the ground" style="left:56px;top:403px;width:164px;height:164px;background:radial-gradient(circle at 45% 45%,#8a8a8c,#4d5a3a 70%,#6b4a2e)"></div>
  <section class="feature" style="left:230px;top:404px;width:220px">
    <h2>BIRDS OF QUEEN MARY REEF</h2>
    <p>-Ocean bird watching boat trips</p>
    <p>-Guided tours of Woodhen and Currawong quarters</p>
    <p>-Weekly lectures at the Queen Mary Reef Museum</p>
    <p>-Weekly screenings of documentaries on Bird and Island Conservation projects</p>
    <p>-Self guided land bird survey tours</p>
  </section>

  <!-- June -->
  <div class="month" style="left:528px;top:352px;width:272px">JUNE 2019&nbsp; Feature Week: 3rd- 9th June</div>
  <div class="photo" role="img" aria-label="Photo of a snorkeller recording underwater survey notes" style="left:456px;top:394px;width:160px;height:160px;background:radial-gradient(circle at 50% 40%,#5fb0d0,#1f6f9e 70%,#134a70)"></div>
  <section class="feature right" style="right:48px;top:398px;width:200px">
    <h2>QUEEN MARY REEF MARINE PARK</h2>
    <p>-Marine pest monitoring with marine park staff</p>
    <p>-Marine plastic &amp; debris clean up activities</p>
    <p>-Screenings of marine conservation documentaries at the museum</p>
    <p>-Weekly lectures on Marine Life at the Queen Mary Reef Museum</p>
    <p>-Marine Activities with local operators</p>
  </section>

  <!-- July -->
  <div class="month" style="left:50px;top:604px;width:280px">JULY 2019&nbsp; Feature Week: 21st – 28th July</div>
  <div class="photo" role="img" aria-label="Photo of a hiker walking through palm forest" style="left:56px;top:660px;width:164px;height:164px;background:radial-gradient(circle at 50% 50%,#9bb06a,#4e6a2c 60%,#7a4a2c)"></div>
  <section class="feature" style="left:232px;top:680px;width:216px">
    <h2>INVASIVE SPECIES</h2>
    <p>-Guided walks to learn about the weed eradication program</p>
    <p>-Weekly lectures on plants of Queen Mary Reef</p>
    <p>-Weekly screenings of documentaries on plant and island conservation projects</p>
    <p>-Guided walks to Mount Gower</p>
    <p>-Local tour guides include commentaries on island plants</p>
  </section>

  <!-- August -->
  <div class="month" style="left:496px;top:610px;width:304px">AUGUST 2019&nbsp; Feature Week: 11th-19th August</div>
  <div class="photo" role="img" aria-label="Photo of a group of volunteers examining invertebrates on a sheet" style="left:495px;top:669px;width:150px;height:150px;background:radial-gradient(circle at 50% 55%,#d9d6cc,#5c7a3a 60%,#2f4a24)"></div>
  <section class="feature right" style="right:44px;top:668px;width:160px">
    <h2>AMAZING INVERTEBRATES</h2>
    <p>-Guided night walks to learn about the island's invertebrates</p>
    <p>-Weekly viewing and presentation of the Queen Mary Reef Phasmid</p>
    <p>-Weekly lectures on invertebrates of Queen Mary Reef at the museum</p>
    <p>-Weekly screenings of documentaries on island conservation projects</p>
  </section>

  <!-- September -->
  <div class="month" style="left:342px;top:874px;width:326px">SEPTEMBER 2019&nbsp; Feature Week: 1st-8th September</div>
  <div class="photo" role="img" aria-label="Photo of hands holding a large black stick insect" style="left:164px;top:884px;width:152px;height:152px;background:radial-gradient(circle at 50% 50%,#e8c8b8,#c9a08c 60%,#8a7a70)"></div>
  <section class="feature" style="left:345px;top:928px;width:310px">
    <h2>PROTECTING PARADISE</h2>
    <p>-Observational snorkel surveys with Marine Ecologists, to assess populations of McCulloch's Anemonefish and other unique fish species</p>
    <p>-Guided snorkel and glass bottom boat tour to assess coral health within the Queen Mary Reef Marine Park</p>
    <p>-Guided walks to learn about the island's conservation history</p>
  </section>

  <footer class="info">
    <p>See the QMR visitor centre for more information about the</p>
    <p>QMR Habitat Helpers program for 2019</p>
    <p class="follow"><span>FOLLOW US!</span><span class="links">www.hhqmr-social.org&nbsp; social@hhqmr</span></p>
  </footer>
</main>
</body>
</html>
```